Business card for technical support company.
FixWiseDesk.com
Business card for technical support company.  - Computers
Creative Brief
Use specific fonts
Up To designer
Professional
Marcus Bell
VP In Charge
482 Alder Lane New York, NY 48213
service@FixWiseDesk.com
This will be used as a mock-up for my business card. Editable Adobe Illustrator or comparable original design file will need to be included with the final design. Also logo can be broken up from the FixWiseDesk.com below it and arranged on the card.
Company logo, website, and possible list of services. Please allow room to add later. 5-6 bullet points
qm71xrb qm71xrb
Nice first drafts everyone. I would like to see how some of these look with a white background instead of black. Nice!
I would like one design but two separate color schemes. Please match the two color schemes of the example logos provided. Thank you!

```html
<!DOCTYPE html>
<html lang="en">
<head>
<meta charset="utf-8">
<title>FixWiseDesk Business Card</title>
<link rel="stylesheet" href="https://fonts.googleapis.com/css2?family=Exo+2:wght@400;600;700&display=swap">
<style>
  :root {
    --page: #2b2b2d;
    --card-white: #ffffff;
    --card-dark: #2a2b2e;
    --card-dark-deep: #1b1c1e;
    --blue: #1f6fd6;
    --blue-deep: #0f4aa8;
    --silver: #cfd3d8;
    --ink: #2a2f38;
    --text-light: #f2f4f7;
    --text-muted: #b9c0ca;
    --brand-blue: #2f7fe0;
  }
  * { margin: 0; padding: 0; box-sizing: border-box; }
  html, body { width: 1200px; height: 698px; overflow: hidden; }
  body {
    background: var(--page);
    font-family: "Exo 2", sans-serif;
    position: relative;
  }
  .card {
    position: absolute;
    top: 200px;
    width: 520px;
    height: 297px;
    border-radius: 14px;
    overflow: hidden;
  }
  .card-back { left: 60px; background: var(--card-white); }
  .card-front {
    left: 620px;
    background: linear-gradient(135deg, #34353a 0%, var(--card-dark) 45%, var(--card-dark-deep) 100%);
  }
  .brand { display: flex; align-items: center; gap: 10px; }
  .brand-mark { width: 26px; height: 26px; background: var(--brand-blue); }
  .brand-name { font-weight: 700; font-size: 30px; letter-spacing: 0.5px; }
  .card-back .brand { position: absolute; left: 50%; top: 92px; transform: translateX(-50%); }
  .card-back .brand-name { color: var(--ink); }
  .card-back .website {
    position: absolute; left: 0; right: 0; top: 170px;
    text-align: center; font-size: 14px; letter-spacing: 3px; color: var(--ink);
  }
  .swoosh { position: absolute; inset: 0; width: 100%; height: 100%; }
  .card-front .brand { position: absolute; left: 40px; top: 58px; }
  .card-front .brand-name { color: var(--text-light); font-size: 28px; }
  .person { position: absolute; left: 40px; top: 138px; color: var(--text-light); }
  .person-name { font-size: 17px; font-weight: 600; letter-spacing: 1px; text-transform: uppercase; }
  .person-title { font-size: 10px; letter-spacing: 1.5px; color: var(--text-muted); text-transform: uppercase; margin-top: 2px; }
  .address {
    position: absolute; left: 40px; bottom: 24px;
    font-size: 10px; line-height: 1.5; color: var(--text-light); font-style: normal;
  }
  .contacts {
    position: absolute; right: 22px; top: 100px;
    list-style: none; color: var(--text-light); font-size: 10px;
  }
  .contacts li {
    display: flex; align-items: center; justify-content: flex-end;
    gap: 8px; height: 20px;
  }
  .contact-icon {
    width: 14px; height: 14px; border-radius: 50%;
    background: var(--text-light); display: flex; align-items: center; justify-content: center;
  }
  .contact-icon svg { width: 9px; height: 9px; }
</style>
</head>
<body>
  <section class="card card-back">
    <div class="brand">
      <span class="brand-mark"></span>
      <span class="brand-name">FixWiseDesk</span>
    </div>
    <p class="website">www.fixwisedesk.com</p>
  </section>

  <section class="card card-front">
    <svg class="swoosh" viewBox="0 0 520 297" preserveAspectRatio="none" aria-hidden="true">
      <defs>
        <linearGradient id="blueBand" x1="0" y1="0" x2="1" y2="1">
          <stop offset="0" stop-color="#3c8ff0"/>
          <stop offset="1" stop-color="#0f4aa8"/>
        </linearGradient>
      </defs>
      <path d="M318 0 C 388 50 368 128 250 162 C 172 186 76 192 0 200 L0 297 L520 297 L520 0 Z" fill="#cfd3d8"/>
      <path d="M330 0 C 400 50 380 132 260 170 C 180 196 80 202 0 210 L0 297 L520 297 L520 0 Z" fill="url(#blueBand)"/>
    </svg>

    <div class="brand">
      <span class="brand-mark"></span>
      <span class="brand-name">FixWiseDesk</span>
    </div>

    <div class="person">
      <p class="person-name">Marcus Bell</p>
      <p class="person-title">VP In Charge</p>
    </div>

    <address class="address">
      482 Alder Lane<br>New York, NY 48213
    </address>

    <ul class="contacts">
      <li>555 204 7781
        <span class="contact-icon"><svg viewBox="0 0 10 10"><path d="M2 1 L4 1 L4.5 3 L3.5 4 Q4.5 6 6 6.5 L7 5.5 L9 6 L9 8 Q5 9 2 5.5 Q1 3.5 2 1Z" fill="#1f6fd6"/></svg></span>
      </li>
      <li>555 204 7782
        <span class="contact-icon"><svg viewBox="0 0 10 10"><rect x="3" y="1" width="4" height="8" rx="0.8" fill="#1f6fd6"/></svg></span>
      </li>
      <li>555 204 7783
        <span class="contact-icon"><svg viewBox="0 0 10 10"><rect x="2" y="4" width="6" height="4" fill="#1f6fd6"/><rect x="3" y="1.5" width="4" height="2.5" fill="#1f6fd6"/></svg></span>
      </li>
      <li>service@FixWiseDesk.com
        <span class="contact-icon"><svg viewBox="0 0 10 10"><rect x="1.5" y="2.5" width="7" height="5" fill="#1f6fd6"/><path d="M1.5 2.5 L5 5.5 L8.5 2.5" stroke="#fff" stroke-width="0.8" fill="none"/></svg></span>
      </li>
      <li>www.fixwisedesk.com
        <span class="contact-icon"><svg viewBox="0 0 10 10"><circle cx="5" cy="5" r="3.5" fill="none" stroke="#1f6fd6" stroke-width="1"/><path d="M1.5 5 H8.5 M5 1.5 V8.5" stroke="#1f6fd6" stroke-width="0.8"/></svg></span>
      </li>
    </ul>
  </section>
</body>
</html>
```